Enrollment openings for summer

I need a postcard design to promote openings at my school. I currently have Corla Press print all of my business cards and have my website with Corla Press, I would like to stick with the design I have. Brightfield School is a therapeutic day school servicing 6-12th grade for bright students with emotional disabilities, autism, learning disabilities and OHI. Although I am trying to promote openings it is not necessarily appropriate for this to be an "upbeat" promotion, more of a softer feel as students come to me when they are struggling significantly and need a safe place to receive an education and support for emotional stability. I will have openings to serve all grades beginning June 3rd (ESY) and for the 15-16 school year. I would also like to communicate that districts can schedule a tour or call for more information. I am looking to market in a 30 miles radius to schools, psychologists, social workers, etc...PLEASE use the look and feel of my current website www.bfsweb.example

Target Market(s)

schools, psychologists, hospital programs, social workers

Industry/Entity Type

Business

Font styles to use
Serif
Decorative

Requirements
Must have
• must match our current design with color and logo, easy to read font
Should not have
• slang, be too bold, softer comfortable feel

```html
<!DOCTYPE html>
<html lang="en">
<head>
<meta charset="utf-8">
<title>Brightfield School – Enrollment Postcard</title>
<link rel="stylesheet" href="https://fonts.googleapis.com/css2?family=Tinos:ital,wght@0,400;0,700;1,400;1,700&display=swap">
<style>
  :root {
    --maroon: #7a1a3a;
    --maroon-deep: #5e1129;
    --brown: #4a2b1d;
    --tan: #b89a72;
    --beige: #dcc9a8;
    --cream: #f1e6d0;
    --paper: #ffffff;
    --stage: #e9e6e2;
    --line-grey: #9a9a9a;
  }
  * { box-sizing: border-box; margin: 0; padding: 0; }
  html, body { width: 1200px; height: 625px; overflow: hidden; }
  body {
    background: var(--stage);
    font-family: "Tinos", "Times New Roman", serif;
  }
  .canvas {
    position: relative;
    width: 1200px;
    height: 625px;
    display: flex;
    align-items: center;
    justify-content: center;
    gap: 30px;
  }
  .postcard {
    position: relative;
    width: 570px;
    height: 380px;
    overflow: hidden;
    box-shadow: 0 6px 18px rgba(0,0,0,0.18);
  }
  .postcard__art {
    position: absolute;
    inset: 0;
    width: 100%;
    height: 100%;
  }
  .abs { position: absolute; }

  /* Front */
  .brand {
    left: 30px; top: 58px;
    color: var(--maroon);
    font-weight: 400;
    font-size: 32px;
    line-height: 1;
    letter-spacing: 0.3px;
    white-space: nowrap;
  }
  .brand__mark {
    display: inline-block;
    width: 12px; height: 12px;
    border-radius: 50%;
    background: var(--maroon);
    margin-right: 7px;
    vertical-align: 5px;
  }
  .tagline {
    color: var(--maroon);
    font-weight: 700;
    font-size: 16px;
    white-space: nowrap;
  }
  .front .tagline { left: 50px; top: 100px; }
  .headline {
    left: 30px; top: 138px;
    width: 300px;
    color: var(--maroon);
    font-weight: 700;
    font-size: 20px;
    line-height: 1.1;
  }
  .about {
    left: 372px; top: 18px;
    width: 186px;
    color: var(--cream);
  }
  .about__title {
    font-weight: 700;
    font-size: 12.5px;
    line-height: 1.15;
    margin-bottom: 6px;
  }
  .about__text {
    font-style: italic;
    font-size: 11.2px;
    line-height: 1.18;
  }
  .seal-text {
    left: 405px; top: 258px;
    width: 90px;
    text-align: center;
    color: var(--maroon);
    font-style: italic;
    font-weight: 700;
    font-size: 11.5px;
    line-height: 1.12;
  }
  .contact { color: var(--cream); }
  .contact__address { font-size: 12px; }
  .contact__web { font-weight: 700; font-size: 13px; margin-top: 1px; }
  .contact__phone { font-weight: 700; font-size: 34px; line-height: 1; margin-top: 2px; }
  .front .contact { left: 30px; top: 296px; }

  /* Back */
  .back .brand { left: 28px; top: 60px; font-size: 28px; }
  .back .brand__mark { width: 10px; height: 10px; vertical-align: 4px; }
  .back .tagline { left: 45px; top: 98px; font-size: 14.5px; }
  .contact__heading { font-weight: 700; font-size: 15px; margin-bottom: 3px; }
  .back .contact { left: 28px; top: 282px; }
  .back .contact__phone { font-size: 27px; }
</style>
</head>
<body>
<main class="canvas">

  <section class="postcard front" aria-label="Postcard front">
    <svg class="postcard__art" viewBox="0 0 570 380">
      <defs>
        <linearGradient id="panelGlow" x1="0" y1="0" x2="1" y2="1">
          <stop offset="0" stop-color="#f3e9d6"/>
          <stop offset="0.6" stop-color="#dcc9a8"/>
          <stop offset="1" stop-color="#c9b08a"/>
        </linearGradient>
      </defs>
      <rect width="570" height="380" fill="var(--maroon)"/>
      <path d="M0 0 H360 V262 C280 276 160 284 0 282 Z" fill="url(#panelGlow)"/>
      <g role="img" aria-label="Soft brown scroll flourish ornament">
        <path d="M0 0 H60 C52 26 28 40 0 44 Z" fill="var(--tan)" opacity="0.5"/>
        <path d="M0 214 C24 228 44 252 56 282 H0 Z" fill="var(--tan)" opacity="0.45"/>
      </g>
      <path d="M0 292 C180 288 380 272 570 248 V380 H0 Z" fill="var(--brown)"/>
      <path d="M0 284 C180 280 380 262 570 236" fill="none" stroke="var(--tan)" stroke-width="7"/>
      <circle cx="450" cy="284" r="60" fill="var(--tan)"/>
      <circle cx="450" cy="284" r="54" fill="var(--maroon)"/>
      <circle cx="450" cy="284" r="49" fill="var(--beige)"/>
    </svg>

    <div class="brand abs"><span class="brand__mark"></span>Brightfield School</div>
    <p class="tagline abs">Where Bright Students Shine!</p>
    <h1 class="headline abs">Opening to serve all grades beginning June 3rd (ESY) for the 2015-2016 school year</h1>

    <div class="about abs">
      <h2 class="about__title">A Therapeutic Day School for Youth with Emotional Challenges</h2>
      <p class="about__text">At Brightfield, we provide students with a safe, therapeutic, and educational environment where they develop skills to become effective learners, gain personal insight, and acquire coping strategies to not only earn school credit, but achieve intellectual and social-emotional potential.</p>
    </div>

    <p class="seal-text abs">Schedule a district tour Today or call for more information</p>

    <address class="contact abs" style="font-style:normal">
      <p class="contact__address">418 Linden Avenue • Maple Grove, IL</p>
      <p class="contact__web">www.bfsweb.example</p>
      <p class="contact__phone">555.014.2736</p>
    </address>
  </section>

  <section class="postcard back" aria-label="Postcard back">
    <svg class="postcard__art" viewBox="0 0 570 380">
      <rect width="570" height="380" fill="var(--paper)"/>
      <path d="M0 266 H318 C350 300 372 340 382 380 H0 Z" fill="var(--maroon)"/>
      <path d="M330 0 C350 130 365 250 410 380 H386 C344 262 330 140 312 0 Z" fill="var(--brown)"/>
      <path d="M350 0 C370 130 386 250 434 380" fill="none" stroke="var(--tan)" stroke-width="6"/>
      <rect x="476" y="18" width="74" height="84" fill="none" stroke="var(--line-grey)" stroke-width="1.5"/>
      <g stroke="var(--line-grey)" stroke-width="1.2">
        <line x1="410" y1="190" x2="550" y2="190"/>
        <line x1="420" y1="225" x2="550" y2="225"/>
        <line x1="432" y1="260" x2="550" y2="260"/>
        <line x1="446" y1="295" x2="550" y2="295"/>
      </g>
    </svg>

    <div class="brand abs"><span class="brand__mark"></span>Brightfield School</div>
    <p class="tagline abs">Where Bright Students Shine!</p>

    <address class="contact abs" style="font-style:normal">
      <p class="contact__heading">Contact us today!</p>
      <p class="contact__address">418 Linden Avenue • Maple Grove, IL</p>
      <p class="contact__web">www.bfsweb.example</p>
      <p class="contact__phone">555.014.2736</p>
    </address>
  </section>

</main>
</body>
</html>
```